Management Company for Associations needs new and improved letterhead

We need a design for letterhead that looks professional. We like designs that can incorporate a lot of space for our letters, a new age professional font, and different styles to choose from. Please use the language in the attached letterhead example. The BRV logo needs to be incorporated in the letterhead; please follow the size requirements for use. We are trying to totally revamp our letterhead.
Industry/Entity Type
Property Management
Font styles to use
Serif
Script
Colors
ec1f27
Requirements
Must have
- BRV Logo in black, Q7 logo, Using both Top & Bottom, Red Color used to match logo color.
Nice to have
- (1 design with a watermark using Q7 logo)

```html
<!DOCTYPE html>
<html lang="en">
<head>
<meta charset="utf-8">
<title>Q7 Letterhead</title>
<link href="https://fonts.googleapis.com/css2?family=Arimo:wght@400;700&display=swap" rel="stylesheet">
<style>
  :root {
    --red: #c00410;
    --ink: #2a2a2a;
    --black: #111111;
    --grey: #9a9a9a;
    --backdrop: #e9e9ea;
    --paper: #ffffff;
  }
  html, body {
    margin: 0;
    width: 1200px;
    height: 1064px;
    overflow: hidden;
    background: var(--backdrop);
    font-family: "Arimo", Arial, sans-serif;
    color: var(--ink);
  }
  .letterhead {
    position: absolute;
    left: 214px;
    top: 32px;
    width: 773px;
    height: 1000px;
    background: var(--paper);
    box-shadow: 0 2px 10px rgba(0,0,0,0.12);
    overflow: hidden;
  }
  .contact {
    position: absolute;
    right: 48px;
    top: 44px;
    font-size: 10px;
    line-height: 1.45;
  }
  .contact .label { color: var(--red); font-weight: 700; }
  .brand {
    position: absolute;
    left: 48px;
    top: 120px;
    display: flex;
    align-items: center;
    gap: 10px;
  }
  .brand-dot {
    width: 22px; height: 22px;
    border-radius: 50%;
    background: var(--red);
  }
  .brand-name {
    font-size: 54px;
    font-weight: 700;
    color: var(--red);
    letter-spacing: -1px;
  }
  .letter {
    position: absolute;
    left: 48px;
    top: 240px;
    width: 470px;
    font-size: 10.5px;
    line-height: 1.45;
  }
  .letter p { margin: 0 0 34px; }
  .letter .date { margin-bottom: 10px; }
  .letter .greeting { margin-bottom: 10px; }
  .greeting strong { display: block; }
  .letter .closing { margin-bottom: 8px; }
  .signature {
    width: 96px; height: 36px;
    background: linear-gradient(90deg, #d6d6d6, #f4f4f4);
    margin-bottom: 6px;
  }
  .signer strong { display: block; }
  .member-badge {
    position: absolute;
    right: 58px;
    top: 600px;
    display: flex;
    align-items: center;
    gap: 10px;
  }
  .badge-square {
    width: 18px; height: 18px;
    background: var(--black);
  }
  .badge-name {
    font-size: 40px;
    color: var(--black);
  }
  .footer-bands {
    position: absolute;
    left: 0; right: 0; bottom: 0;
  }
  .footer-bands .rule-grey { height: 6px; background: var(--grey); }
  .footer-bands .gap { height: 4px; }
  .footer-bands .rule-black { height: 3px; background: var(--black); }
  .footer-bands .band-red { height: 150px; background: var(--red); margin-top: 4px; }
</style>
</head>
<body>
  <main class="letterhead">
    <div class="contact">
      <div><span class="label">Toll Free:</span> 800-555-0142</div>
      <div><span class="label">Email:</span> info@q7managers.com</div>
      <div><span class="label">Web:</span> www.q7managers.com</div>
    </div>

    <div class="brand">
      <span class="brand-dot"></span>
      <span class="brand-name">Q7</span>
    </div>

    <section class="letter">
      <p class="date">July 2, 2012</p>
      <p class="greeting"><strong>Dear CH,</strong>ABC Building, def St., Country Name</p>
      <p>is simply dummy text of the printing and typesetting industry. Lorem Ipsum has been the industry's standard dummy text ever since the 1500s, when an unknown printer took a galley of type and scrambled it to make a type specimen book. It has survived not only five centuries, but also the leap into electronic typesetting, remaining essentially unchanged. It was popularised in the 1960s with the release of Linefold sheets containing Lorem Ipsum passages, and more recently with desktop publishing software like Pressline Studio including versions of Lorem Ipsum.</p>
      <p>is simply dummy text of the printing and typesetting industry. Lorem Ipsum has been the industry's standard dummy text ever since the 1500s, when an unknown printer took a galley of type and scrambled it to make</p>
      <p>is simply dummy text of the printing and typesetting industry. Lorem Ipsum has been the industry's standard dummy text ever since the 1500s, when an unknown printer took a galley of type and scrambled it to make a type specimen book. It has survived not only five centuries, but also the leap into electronic typesetting, remaining essentially unchanged. It was popularised in the 1960s with the release of Linefold sheets containing Lorem Ipsum passages, and more recently with desktop publishing software like Pressline Studio including versions of Lorem Ipsum.</p>
      <p class="closing">Best Regards,</p>
      <div class="signature" role="img" aria-label="Handwritten signature"></div>
      <div class="signer"><strong>Daniel Hart</strong>Director<br>ABC Building, def St., Country Name</div>
    </section>

    <div class="member-badge">
      <span class="badge-square"></span>
      <span class="badge-name">BRV</span>
    </div>

    <footer class="footer-bands" aria-hidden="true">
      <div class="rule-grey"></div>
      <div class="gap"></div>
      <div class="rule-black"></div>
      <div class="band-red"></div>
    </footer>
  </main>
</body>
</html>
```